Brisk Nook needs a packaging design

Hello!

I need an eye-catching package design for Brisk Nook mobile accessories. The products inside the box package include a bluetooth speaker and a power bank.

This is under our brandname called Brisk Nook. The text should be in the picture, no matter how the design looks.

I have attached pictures of the products. If you think that there will not be well with the images it is ok. Then these texts be included:
Bluetooth Speaker
Power Bank

This is our slogan:
Music + Power. It's your imagination that sets the limits!

The image will be printed on a carton pack containing with four color printing. Customising the picture for the type of print.

Should be in 300 DPI High resolution.

Please check the attached pictures where your design will be printed.
Also, I attached design inspiration images for reference. Feel free to do something similar like that.

For the size and dimensions please refer to this attachment:

So remember, the important thing is the design. Do your absolute best!
Updates

Reason: Hello everyone! I would like to see a design without the images of the accessories. Only text. I also dont want the text "Its you imagination that sets...". Thank you!

Target Market(s)

Mobile accessories

Industry/Entity Type

Electronics

Requirements
Must have
• This text:
• Brisk Nook
Nice to have
• Music + Power.

```html
<!DOCTYPE html>
<html lang="en">
<head>
<meta charset="utf-8">
<title>Brisk Nook — Packaging</title>
<link rel="stylesheet" href="https://fonts.googleapis.com/css2?family=Open+Sans:wght@400;700;800&display=swap">
<style>
  :root {
    --stage: #3a3a3a;
    --panel-deep: #07080a;
    --panel-mid: #15181d;
    --panel-light: #2a3038;
    --hex-glow: #5a7ea3;
    --brand-blue: #7fcff0;
    --sub-grey: #5d646c;
    --side-black: #0a0a0a;
    --side-text: #2e2e2e;
    --badge-grey: #b9bcc0;
    --white: #ffffff;
  }
  * { box-sizing: border-box; margin: 0; padding: 0; }
  html, body {
    width: 1200px; height: 1000px; overflow: hidden;
    background: var(--stage);
    font-family: "Open Sans", Arial, sans-serif;
  }
  .dieline {
    position: absolute; left: 205px; top: 150px;
    display: flex; height: 700px;
    box-shadow: 0 20px 50px rgba(0,0,0,.45);
  }
  .front-panel {
    position: relative; width: 700px; height: 700px; overflow: hidden;
    background: linear-gradient(160deg, var(--panel-mid) 0%, var(--panel-deep) 60%, #050506 100%);
  }
  .hex-texture {
    position: absolute; inset: 0;
    background:
      radial-gradient(ellipse at 30% 20%, rgba(90,126,163,.28), transparent 55%),
      linear-gradient(150deg, var(--panel-light) 0%, var(--panel-mid) 40%, var(--panel-deep) 75%);
  }
  .sweep-band {
    position: absolute; inset: 0; width: 700px; height: 700px;
  }
  .brand-block {
    position: absolute; left: 150px; top: 455px; width: 470px; text-align: center;
  }
  .brand-name {
    display: flex; align-items: center; justify-content: center; gap: 16px;
    font-size: 64px; font-weight: 800; letter-spacing: 2px;
    color: var(--brand-blue); text-transform: uppercase; line-height: 1;
  }
  .brand-dot {
    width: 26px; height: 26px; border-radius: 50%; background: var(--brand-blue);
  }
  .product-line {
    margin-top: 12px; font-size: 17px; font-weight: 700;
    letter-spacing: 5px; color: var(--sub-grey);
  }
  .retailer-badge {
    position: absolute; right: 30px; bottom: 60px; text-align: center;
    font-weight: 700; font-size: 16px; line-height: 1.25;
  }
  .retailer-badge .badge-top {
    display: block; padding: 1px 6px; border: 1px solid var(--white);
    background: var(--badge-grey); color: #2a2a2a;
  }
  .retailer-badge .badge-bottom { display: block; color: var(--white); margin-top: 3px; }
  .side-panel {
    position: relative; width: 90px; height: 700px; background: var(--side-black);
    border-left: 1px solid #000;
  }
  .slogan {
    position: absolute; left: 50%; top: 300px;
    transform: translate(-50%, -50%) rotate(-90deg);
    white-space: nowrap; font-size: 34px; font-weight: 700;
    letter-spacing: 8px; color: var(--side-text); text-transform: uppercase;
  }
</style>
</head>
<body>
  <main class="dieline">
    <section class="front-panel">
      <div class="hex-texture" role="img" aria-label="Dark hexagonal mesh texture with soft blue edge glow"></div>
      <svg class="sweep-band" viewBox="0 0 700 700" aria-hidden="true">
        <path d="M0 380 Q300 300 700 160 L700 700 L0 700 Z" fill="rgba(0,0,0,.45)"/>
        <path d="M0 380 Q300 300 700 160" fill="none" stroke="rgba(120,140,160,.35)" stroke-width="2"/>
        <path d="M0 560 Q320 470 700 330" fill="none" stroke="rgba(120,140,160,.25)" stroke-width="2"/>
      </svg>
      <div class="brand-block">
        <h1 class="brand-name"><span>Brisk Nook</span><span class="brand-dot"></span></h1>
        <p class="product-line">Bluetooth Speaker + Power Bank</p>
      </div>
      <div class="retailer-badge">
        <span class="badge-top">POCKET GEAR</span>
        <span class="badge-bottom">SUPPLY</span>
      </div>
    </section>
    <aside class="side-panel">
      <p class="slogan">Music + Power</p>
    </aside>
  </main>
</body>
</html>
```